SilverLedgerOak - Double Sided Business Card

We are looking for design options or our business cards. We are a Business Solutions and HR solutions Provider - the theme is business, for this card.

Our brand colours are represented within our logo.

Details needed to be put on the front of the business card are:

Employees name: [Sample Name]
Role: [Sample Role]

Address: Suite 4 - Level 3/48 Halloran Avenue Brennadale NSW 2164
M: 0000 000 000
P: 1300 847 213
F: 1300 847 286
E: sample@silverledgeroak.com.au
www.silverledgeroak.com.au
Updates

Reason: Hello, could we please increase our deadline by 5 days. Thanking you, Tess

Target Market(s)

Business Owners, also Candidates looking for Employment

Industry/Entity Type

Business

Contact Information for Business Card

Role: [Sample Role]

M: 0000 000 000
P: 1300 847 213
F: 1300 847 286

Font styles to use
Sans Serif

Colors
3276b5
3176b5
0455a3
85abd2
cfdeed
ffffff
000000
1b1b1b
757575

Requirements
Must have
• Details needed to be put on the front of the business card are:
• Employees name: [Sample Name]
• Role: [Sample Role]
• Address: Suite 4 - Level 3/48 Halloran Avenue Brennadale NSW 2164
• M: 0000 000 000
• P: 1300 847 213
• F: 1300 847 286
• E: sample@silverledgeroak.com.au
• www.silverledgeroak.com.au
Nice to have
• Simplicity, clean and professional.

```html
<!DOCTYPE html>
<html lang="en">
<head>
<meta charset="utf-8">
<title>SilverLedgerOak Business Card</title>
<link href="https://fonts.googleapis.com/css2?family=Roboto:wght@300;400;700;900&display=swap" rel="stylesheet">
<style>
  :root {
    --bg: #1e1e1e;
    --white: #ffffff;
    --blue: #3276b5;
    --blue-deep: #1d5ea8;
    --navy: #0f2a4a;
    --ink: #1b3a63;
    --faint: #e3e6ea;
  }
  * { margin: 0; padding: 0; box-sizing: border-box; }
  html, body { width: 960px; height: 1200px; overflow: hidden; }
  body {
    background: var(--bg);
    font-family: "Roboto", sans-serif;
    position: relative;
  }
  .card {
    position: absolute;
    left: 120px;
    width: 720px;
    height: 410px;
    border-radius: 28px;
    overflow: hidden;
  }
  .card-front { top: 110px; background: var(--white); }
  .card-back { top: 680px; background: var(--blue); }

  .brand {
    position: absolute;
    left: 0; right: 0; top: 150px;
    display: flex; align-items: center; justify-content: center; gap: 14px;
  }
  .brand-mark { width: 34px; height: 34px; background: var(--blue); }
  .brand-name {
    font-weight: 900; font-size: 44px; color: var(--ink); letter-spacing: 0.5px;
  }
  .brand-rule {
    position: absolute; left: 170px; right: 170px; top: 218px;
    height: 2px; background: var(--ink);
  }
  .tagline {
    position: absolute; left: 0; right: 0; top: 232px;
    text-align: center; font-weight: 700; font-size: 15px; color: var(--ink);
  }

  .back-shapes { position: absolute; inset: 0; }
  .faint-name {
    position: absolute; right: 30px; top: 110px;
    font-weight: 900; font-size: 40px; color: var(--faint);
  }
  .person { position: absolute; left: 40px; top: 48px; color: var(--white); }
  .person-name { font-weight: 700; font-size: 28px; }
  .person-role { font-weight: 300; font-size: 21px; margin-top: 2px; }
  .contacts {
    position: absolute; left: 40px; top: 165px; list-style: none;
    color: var(--white); font-size: 17px;
  }
  .contacts li { display: flex; align-items: center; gap: 12px; height: 30px; }
  .contacts svg { width: 18px; height: 18px; fill: var(--white); flex: none; }
  .address {
    position: absolute; right: 40px; bottom: 40px;
    color: var(--white); font-size: 18px; text-align: right; line-height: 1.3;
  }
</style>
</head>
<body>

<section class="card card-front">
  <div class="brand">
    <span class="brand-mark"></span>
    <span class="brand-name">SilverLedgerOak</span>
  </div>
  <div class="brand-rule"></div>
  <p class="tagline">Guiding growing firms of every size toward their full promise</p>
</section>

<section class="card card-back">
  <svg class="back-shapes" viewBox="0 0 720 410" preserveAspectRatio="none">
    <defs>
      <linearGradient id="blueFade" x1="0" y1="0" x2="0" y2="1">
        <stop offset="0" stop-color="#3a7cbd"/>
        <stop offset="1" stop-color="#1d5ea8"/>
      </linearGradient>
    </defs>
    <rect width="720" height="410" fill="url(#blueFade)"/>
    <polygon points="240,0 720,0 720,210 560,290 470,230" fill="#ffffff"/>
    <polygon points="470,230 560,290 720,210 720,410 320,410" fill="#0f2a4a"/>
  </svg>
  <span class="faint-name">SilverLedgerOak</span>

  <div class="person">
    <p class="person-name">Lorem Ipsum</p>
    <p class="person-role">Director</p>
  </div>

  <ul class="contacts">
    <li><svg viewBox="0 0 24 24"><path d="M7 1h10a2 2 0 0 1 2 2v18a2 2 0 0 1-2 2H7a2 2 0 0 1-2-2V3a2 2 0 0 1 2-2zm0 3v14h10V4z"/></svg>0000 000 000</li>
    <li><svg viewBox="0 0 24 24"><path d="M6.6 10.8a15 15 0 0 0 6.6 6.6l2.2-2.2a1 1 0 0 1 1-.25 11.4 11.4 0 0 0 3.6.57 1 1 0 0 1 1 1V20a1 1 0 0 1-1 1A17 17 0 0 1 3 4a1 1 0 0 1 1-1h3.5a1 1 0 0 1 1 1c0 1.25.2 2.45.57 3.6a1 1 0 0 1-.25 1z"/></svg>1300 847 213</li>
    <li><svg viewBox="0 0 24 24"><path d="M6 2h12v5H6zM3 8h18a2 2 0 0 1 2 2v7h-4v5H5v-5H1v-7a2 2 0 0 1 2-2zm4 8v4h10v-4z"/></svg>1300 847 286</li>
    <li><svg viewBox="0 0 24 24"><path d="M2 5h20v14H2zm2 2v.5l8 5 8-5V7z"/></svg>sample@silverledgeroak.com.au</li>
    <li><svg viewBox="0 0 24 24"><path d="M12 2a10 10 0 1 0 0 20 10 10 0 0 0 0-20zm1 2.1c1.3.9 2.3 3 2.6 5.9h-5.2c.3-2.9 1.3-5 2.6-5.9zM4.1 11h4.3c.1 1.9.4 3.6 1 5H5.4a8 8 0 0 1-1.3-5zm0-2a8 8 0 0 1 4.6-5 13 13 0 0 0-1.3 5zm11.5 2a14 14 0 0 1-1 5h-5.2a14 14 0 0 1-1-5zm.9 0h3.4a8 8 0 0 1-1.3 5h-3.1c.6-1.4.9-3.1 1-5zm3.4-2h-3.4a13 13 0 0 0-1.3-5 8 8 0 0 1 4.7 5z"/></svg>www.silverledgeroak.com.au</li>
  </ul>

  <p class="address">Suite 4 - Level 3/48<br>Halloran Avenue<br>Brennadale NSW 2164</p>
</section>

</body>
</html>
```